Upscale business cards needed for Board of Directors

We need professional business cards created for members of our family business Board of Directors. We would like these relatively simple and straightforward, but also with a unique element to set them apart. Probably stick with neutral and simple colors - white, grey etc. We need space for the traditional elements, including name, title, address, email/phone number. And we will be creating several from this template so it needs to be template that is easy to switch information in and out of.
Business
See description

```html
<!DOCTYPE html>
<html lang="en">
<head>
<meta charset="utf-8">
<title>Harborline Holdings – Business Card</title>
<link rel="stylesheet" href="https://fonts.googleapis.com/css2?family=Arimo:wght@400&display=swap">
<style>
  :root {
    --backdrop: #e9e6e1;
    --paper: #ffffff;
    --paper-shade: #f1f1f1;
    --ink: #2a2a2a;
    --night: #0d0d0d;
    --sand: #c9bb9c;
    --sand-soft: #d8ccb1;
    --light-text: #f4f4f4;
  }
  * { box-sizing: border-box; margin: 0; padding: 0; }
  html, body {
    width: 1200px; height: 858px; overflow: hidden;
    background: var(--backdrop);
  }
  .canvas {
    width: 1200px; height: 858px;
    display: flex; align-items: center; justify-content: center; gap: 40px;
  }
  .card {
    width: 540px; height: 309px;
    background: linear-gradient(135deg, var(--paper) 60%, var(--paper-shade));
    box-shadow: 0 10px 26px rgba(0,0,0,.18);
    position: relative; overflow: hidden;
    font-family: "Arimo", sans-serif;
  }
  .company-name {
    font-family: "Arimo", sans-serif;
    font-weight: 400;
    font-size: 34px;
    line-height: 1;
    color: var(--ink);
    white-space: nowrap;
  }

  /* front */
  .front .brand-area {
    position: absolute; left: 0; top: 0; width: 100%; height: 150px;
    display: flex; align-items: center; justify-content: center;
  }
  .front .accent-band {
    position: absolute; left: 0; top: 150px; width: 100%; height: 9px;
    background: var(--sand);
  }
  .front .info-area {
    position: absolute; left: 0; top: 159px; width: 100%; bottom: 0;
    background: var(--night);
    display: flex; align-items: center;
  }
  .person { width: 210px; padding-left: 44px; }
  .person .name { color: var(--light-text); font-size: 20px; }
  .person .title { color: var(--sand-soft); font-size: 15px; margin-top: 3px; }
  .divider { width: 1px; height: 82px; background: var(--light-text); margin-right: 24px; }
  .contacts { list-style: none; }
  .contacts li {
    display: flex; align-items: center; gap: 10px;
    color: var(--light-text); font-size: 15px; margin: 7px 0;
  }
  .contacts svg { width: 16px; height: 16px; flex: none; }

  /* back */
  .back { display: flex; align-items: center; justify-content: center; }
</style>
</head>
<body>
<main class="canvas">
  <section class="card front">
    <div class="brand-area">
      <p class="company-name">Harborline Holdings</p>
    </div>
    <div class="accent-band"></div>
    <div class="info-area">
      <div class="person">
        <p class="name">Owen Castell</p>
        <p class="title">Managing Director</p>
      </div>
      <div class="divider"></div>
      <ul class="contacts">
        <li>
          <svg viewBox="0 0 16 16"><rect width="16" height="16" rx="2" fill="var(--sand)"/><path d="M5 3.5l2 2-1 1.3c.6 1.3 1.6 2.3 2.9 2.9l1.3-1 2 2-1.2 1.6C8 12 4 8 3.7 4.8z" fill="var(--night)"/></svg>
          <span>021-555-0137</span>
        </li>
        <li>
          <svg viewBox="0 0 16 16"><rect width="16" height="16" rx="2" fill="var(--sand)"/><rect x="3" y="4.5" width="10" height="7" fill="none" stroke="var(--night)" stroke-width="1.2"/><path d="M3 4.5l5 4 5-4" fill="none" stroke="var(--night)" stroke-width="1.2"/></svg>
          <span>office@harborline.com</span>
        </li>
        <li>
          <svg viewBox="0 0 16 16"><rect width="16" height="16" rx="2" fill="var(--sand)"/><path d="M8 13s-3.5-3.8-3.5-6.3a3.5 3.5 0 017 0C11.5 9.2 8 13 8 13z" fill="var(--night)"/><circle cx="8" cy="6.7" r="1.3" fill="var(--sand)"/></svg>
          <span>480 N Calder Rd</span>
        </li>
      </ul>
    </div>
  </section>

  <section class="card back">
    <p class="company-name">Harborline Holdings</p>
  </section>
</main>
</body>
</html>
```